The Maple Sprout Clinic needs a Letterhead

We are a bilingual pediatric clinic located in Montreal, Canada.

Our english name is Maple Sprout Clinic
Our french name is Clinique du petit ruisseau

We offer complete care for children including general pediatric care, pediatric specialist care such as Ear, Nose and Throat, Urology, Neurology and Adolescent Medicine. We also have paramedical specialists such as psychologists, social workers, occupational therapists, speech and language pathologists.

The letterhead must use and be harmonious with our new logo. See Design #4923293. We need two types of letterhead. One for a the Logo and both english and french names on the top and the second with the list of current staff on the left. I have uploaded two old examples for you to see. Thanks and good luck.

Font styles to use
Sans Serif

Colors
3176b5
9d9d9d

Requirements
Must have
• Include our logo.
Nice to have
• Most of our printing is done in black and white. So a grayscale design is fine.
I have included a color and grayscale versions of our logo.

We prefer clean modern designs.

```html
<!DOCTYPE html>
<html lang="fr">
<head>
<meta charset="utf-8">
<title>Maple Sprout Clinic – Letterhead</title>
<link rel="stylesheet" href="https://fonts.googleapis.com/css2?family=Source+Sans+3:wght@400;700&display=swap">
<style>
  :root {
    --paper: #ffffff;
    --frame: #d6d6d6;
    --ink: #111111;
    --band: #000000;
    --band-text: #ffffff;
    --muted: #8c8c8c;
    --brand-grey: #9d9d9d;
  }
  * { margin: 0; padding: 0; box-sizing: border-box; }
  html, body { width: 900px; height: 1200px; overflow: hidden; background: var(--paper); }
  body { font-family: "Source Sans 3", Arial, sans-serif; color: var(--ink); position: relative; }

  .sheet {
    position: absolute; left: 42px; top: 22px; width: 816px; height: 1156px;
    border: 1px solid var(--frame); background: var(--paper);
  }

  .brand { position: absolute; top: 70px; left: 0; width: 900px; height: 68px; }
  .brand-name {
    position: absolute; top: 0; font-size: 18.5px; line-height: 21px;
    font-weight: 400; color: var(--brand-grey);
  }
  .brand-name--fr { right: 494px; text-align: right; }
  .brand-name--en { left: 492px; text-align: left; }
  .brand-dot { position: absolute; left: 415px; top: -1px; width: 70px; height: 70px; border-radius: 50%; background: var(--brand-grey); }

  .staff-band {
    position: absolute; left: 42px; top: 1061px; width: 816px; height: 24px; background: var(--band);
  }
  .staff-col { position: absolute; top: 1063px; font-size: 9px; line-height: 11px; }
  .staff-col h3 { font-size: 9px; font-weight: 700; color: var(--band-text); line-height: 10px; }
  .staff-col .en { display: block; font-size: 9px; font-weight: 700; color: var(--muted); line-height: 11px; }
  .staff-col ul { list-style: none; margin-top: 10px; font-size: 9px; line-height: 11px; color: var(--ink); }
  .staff-col b { font-weight: 700; }
</style>
</head>
<body>
  <div class="sheet"></div>

  <header class="brand">
    <div class="brand-name brand-name--fr">Clinique du<br>petit<br>ruisseau</div>
    <div class="brand-dot"></div>
    <div class="brand-name brand-name--en">Maple<br>Sprout<br>Clinic</div>
  </header>

  <div class="staff-band"></div>

  <section class="staff-col" style="left:82px">
    <h3>ADDRESSE<span class="en">ADDRESS</span></h3>
    <ul>
      <li>2250 boul. des Érables</li>
      <li>Suite 210</li>
      <li>Montréal, Qc</li>
      <li>H4R 2K8</li>
      <li><b>Tél.</b> (514) 555-0142</li>
      <li><b>Fax.</b> (514) 555-0187</li>
    </ul>
  </section>

  <section class="staff-col" style="left:204px">
    <h3>PÉDIATRES<span class="en">PEDIATRICIANS</span></h3>
    <ul>
      <li>H. Bergeron</li>
      <li>J. Colton</li>
      <li>R. Lindqvist</li>
      <li>D. Marchal</li>
      <li>N. Tremblant</li>
      <li>M.Harlow</li>
      <li>D.Fenwick</li>
    </ul>
  </section>

  <section class="staff-col" style="left:292px">
    <h3>NEUROLOGUE<span class="en">NEUROLOGIST</span></h3>
    <ul><li>M. Dorval</li></ul>
  </section>

  <section class="staff-col" style="left:372px">
    <h3>O.R.L.<span class="en">E.N.T.</span></h3>
    <ul><li>T. Arslan</li></ul>
  </section>

  <section class="staff-col" style="left:428px">
    <h3>UROLOGUE<span class="en">UROLOGIST</span></h3>
    <ul><li>R. Pollard</li></ul>
  </section>

  <section class="staff-col" style="left:501px">
    <h3>PSYCHOLOGUES<span class="en">PSYCHOLOGISTS</span></h3>
    <ul><li>H. Lemieux</li><li>A. Roussel</li></ul>
  </section>

  <section class="staff-col" style="left:590px">
    <h3>TRAVAILLEUSE<span class="en">SOCIAL WORKER</span></h3>
    <ul><li>S. Gable</li></ul>
  </section>

  <section class="staff-col" style="left:698px">
    <h3>DIETETISTE<span class="en">DIETICIAN</span></h3>
    <ul><li>L. Santoro</li></ul>
  </section>

  <section class="staff-col" style="left:771px">
    <h3>GERANTE<span class="en">MANAGER</span></h3>
    <ul><li>C.Valcourt</li></ul>
  </section>
</body>
</html>
```